Business Card for Dental Surgery

Professional and vibrant business card for dental surgery

Other side to incorporate space for appointment date and times

My website is www.larkvaledental.com.au

Target Market(s)

All

Industry/Entity Type

Dental

Requirements
Must have
• Catchy
Phone no, internet etc
Nice to have
• portray same image as website.
on reverse appointment side:
"Please give 24 hours notice if you cannot attend"
Nice colours

```html
<!DOCTYPE html>
<html lang="en">
<head>
<meta charset="utf-8">
<title>Larkvale Dental – Business Card</title>
<link rel="stylesheet" href="https://fonts.googleapis.com/css2?family=Open+Sans:wght@400;700&display=swap">
<style>
  :root {
    --purple: #9547c9;
    --lime: #a6e64a;
    --slate: #5f6a6a;
    --slate-soft: #6f7878;
    --ghost: #c6cccc;
    --rule: #6f7777;
    --edge: #b9c0c0;
    --white: #ffffff;
  }
  * { box-sizing: border-box; margin: 0; padding: 0; }
  html, body {
    width: 1050px; height: 1200px; overflow: hidden;
    background: var(--white);
    font-family: "Open Sans", Arial, sans-serif;
  }
  .sheet { position: relative; width: 1050px; height: 1200px; }

  .card {
    position: absolute; left: 52px; width: 924px; height: 528px;
    border: 1.5px solid var(--edge); background: var(--white); overflow: hidden;
  }
  .card--front { top: 33px; }
  .card--back { top: 618px; }

  .side-label {
    position: absolute; left: 56px; font-size: 22px; color: var(--slate-soft);
  }
  .side-label--front { top: 562px; }
  .side-label--back { top: 1148px; }

  /* front */
  .brand-name {
    position: absolute; left: 22px; top: 6px;
    font-size: 108px; font-weight: 700; letter-spacing: -4px;
    color: var(--purple); line-height: 1.2; white-space: nowrap;
  }
  .dentists {
    position: absolute; left: 576px; top: 150px;
    color: var(--slate); font-size: 27px; line-height: 34px; letter-spacing: 0.5px;
  }
  .dentists .quals { font-size: 14px; letter-spacing: 0.5px; margin-left: 4px; }
  .wave { position: absolute; left: 0; top: 0; width: 924px; height: 528px; }
  .contact {
    position: absolute; top: 358px; color: var(--white);
    font-size: 28px; line-height: 42px; letter-spacing: 0.8px;
  }
  .contact--address { left: 62px; }
  .contact--address .practice { font-size: 32px; }
  .contact--online { left: 451px; }

  /* back */
  .appt-title {
    position: absolute; left: 0; right: 0; top: 18px; text-align: center;
    font-size: 58px; color: var(--slate); letter-spacing: 2px;
  }
  .weekdays {
    position: absolute; left: 44px; right: 44px; top: 118px;
    display: flex; justify-content: space-between;
    font-size: 21px; color: var(--slate);
  }
  .field {
    position: absolute; font-size: 20px; color: var(--slate);
    display: flex; align-items: flex-end; gap: 8px;
  }
  .field .line { border-bottom: 1.5px solid var(--rule); height: 1px; margin-bottom: 5px; }
  .field--date { left: 60px; top: 186px; }
  .field--date .line { width: 272px; }
  .field--time { left: 500px; top: 186px; }
  .field--time .line { width: 272px; }
  .field--notes { left: 60px; top: 256px; }
  .field--notes .line { width: 735px; }
  .note-line {
    position: absolute; left: 60px; width: 810px; border-bottom: 1.5px solid var(--rule);
  }
  .note-line--2 { top: 322px; }
  .note-line--3 { top: 371px; }
  .brand-name--faint {
    top: 378px; left: 22px; color: var(--ghost);
  }
</style>
</head>
<body>
<main class="sheet">

  <section class="card card--front" aria-label="Card front">
    <svg class="wave" viewBox="0 0 924 528" aria-hidden="true">
      <path d="M0 302 C120 312 170 345 300 338 C420 330 480 286 620 284 C740 282 840 300 924 326 L924 528 L0 528 Z" fill="var(--purple)"/>
      <path d="M0 316 C120 326 170 359 300 352 C420 344 480 300 620 298 C740 296 840 314 924 340 L924 528 L0 528 Z" fill="var(--lime)"/>
    </svg>

    <div class="brand-name">Larkvale Dental</div>

    <div class="dentists">
      <div>Dr. Martin Hale<span class="quals">BDS</span></div>
      <div>Dr. Grace Lin<span class="quals">BDS FRACDS</span></div>
    </div>

    <address class="contact contact--address" style="font-style:normal">
      <div class="practice">Larkvale Dental</div>
      <div>18 Larkvale Rd.</div>
      <div>Larkvale. NSW 2299</div>
    </address>

    <div class="contact contact--online">
      <div>Phone: 02 9411 3275</div>
      <div>admin@larkvaledental.com.au</div>
      <div>www.larkvaledental.com.au</div>
    </div>
  </section>
  <div class="side-label side-label--front">front</div>

  <section class="card card--back" aria-label="Card back">
    <h2 class="appt-title" style="font-weight:400">Your Next Appointment:</h2>
    <div class="weekdays">
      <span>Monday</span><span>Tuesday</span><span>Wednesday</span><span>Thursday</span><span>Friday</span><span>Saturday</span><span>Sunday</span>
    </div>
    <div class="field field--date"><span>Date:</span><span class="line"></span></div>
    <div class="field field--time"><span>Time:</span><span class="line"></span></div>
    <div class="field field--notes"><span>Notes:</span><span class="line"></span></div>
    <div class="note-line note-line--2"></div>
    <div class="note-line note-line--3"></div>
    <div class="brand-name brand-name--faint">Larkvale Dental</div>
  </section>
  <div class="side-label side-label--back">back</div>

</main>
</body>
</html>
```